Plakat-Design für Punkteabbau durch Teilnahme an einem Fahreignungsseminar (FES)
Zielgruppe
Wir sind die Dachorganisation deutscher Fahrschulen. Die Zielgruppe für das Plakat sind Kraftfahrer von 18 - 80 Jahren
Aufgabenstellung
Wir benötigen einen Plakatentwurf für die Bewerbung für Seminare für Kraftfahrer (Fahreignungsseminare (FES)), die einen Punkt tilgen wollen oder auch ohne „Punkterabatt“ teilnehmen wollen.
Fahrschulen sollen das Plakat in ihren Schaufenster aushängen, für die Seminare werben und gleichzeitig gute Beratung anbieten.
Es soll pfiffig sein und neugierig machen.
Texte könnten alternativ sein:
Wir helfen Ihnen Punkte los zu werden.
Punkte in Flensburg?
Hilfe hier – wir beraten Sie gerne.
Punkteabbauseminare hier möglich
Farben Logo:
Blau - 0 - 66 - 137
Gelb - 252 - 191 - 0

```html
<!DOCTYPE html>
<html lang="de">
<head>
<meta charset="utf-8">
<title>Plakat – Punkte in Flensburg?</title>
<link href="https://fonts.googleapis.com/css2?family=Jost:wght@700;800;900&display=swap" rel="stylesheet">
<style>
  :root {
    --blue: rgb(0, 66, 137);
    --yellow: rgb(252, 191, 0);
    --ink: #111111;
    --paper: #ffffff;
    --backdrop: #d4d4d4;
  }
  * { margin: 0; padding: 0; box-sizing: border-box; }
  html, body {
    width: 1200px;
    height: 675px;
    overflow: hidden;
    background: var(--backdrop);
  }
  .poster {
    position: absolute;
    left: 378px;
    top: 22px;
    width: 445px;
    height: 630px;
    background: var(--paper);
    font-family: "Jost", "Futura", sans-serif;
    overflow: hidden;
  }
  .headline {
    position: absolute;
    left: 16px;
    top: 34px;
    color: var(--blue);
    font-weight: 900;
    font-size: 38px;
    line-height: 36px;
    text-transform: uppercase;
    letter-spacing: 0.5px;
    transform: rotate(-5deg);
    transform-origin: left top;
  }
  .headline span { display: block; }
  .headline span:nth-child(2) { transform: rotate(-1deg); }
  .headline span:nth-child(3) { transform: rotate(-2deg); margin-left: 4px; }
  .headline span:nth-child(4) { transform: rotate(-1deg); margin-left: 6px; }
  .brand {
    position: absolute;
    right: 22px;
    top: 52px;
    color: var(--blue);
    font-weight: 800;
    font-size: 24px;
    letter-spacing: 0;
  }
  .offer {
    position: absolute;
    left: 0;
    right: 0;
    top: 440px;
    text-align: center;
  }
  .offer-question {
    color: var(--yellow);
    font-weight: 900;
    font-size: 41px;
    line-height: 44px;
  }
  .offer-help {
    color: var(--blue);
    font-weight: 900;
    font-size: 37px;
    line-height: 38px;
  }
  .offer-details {
    margin-top: 6px;
    color: var(--ink);
    font-weight: 800;
    font-size: 18px;
    line-height: 17px;
    letter-spacing: 0.3px;
  }
</style>
</head>
<body>
  <main class="poster">
    <h1 class="headline">
      <span>Hier gibt</span>
      <span>es nichts</span>
      <span>mehr zu</span>
      <span>sehen!</span>
    </h1>
    <div class="brand">Quintar</div>
    <section class="offer">
      <p class="offer-question">Punkte in Flensburg?</p>
      <p class="offer-help">Hilfe hier –<br>Wir beraten Sie gerne!</p>
      <p class="offer-details">Wie bieten Seminare für Kraftfahrer (FES)<br>die einen Punkt tilgen wollen. Teilnahme<br>auch ohne „Punkterabatt“ möglich.</p>
    </section>
  </main>
</body>
</html>
```